Health Coach needs a creative and catchy Chatnook Ad Image to increase page likes

I have just recently launched a health coaching business and would like to increase my Chatnook awareness and page likes.
I plan on doing a “page liking” campaign through Chatnook and want a creative, catchy and unique image to help make my campaign successful.
I want a versatile image, as I am aiming to run this campaign on Chatnook for a while (few months).
The image is to be 1200 x 444 pixels, with an image ratio of 8:3, and because it is going on Chatnook it cannot have any overlaid text (or very little).
So, the image will have to be very visually appealing and catchy!
I am happy for some creative illustrations and drawings to be used to help portray my message (please see attached for some sample pictures)
I would like the image to portray the following:
-health
-happiness
-change
Some of my key messages that you could include:
-holistic health
-health & wellness
-health, nutrition, lifestyle
-Food, fitness, happiness

In addition, a call to action that could be incorporated could be:
"i can help you"
..or something similar (but only if this can fit).

I have attached some images of myself to be used.

Target Market(s)

People looking for health and fitness advice

Industry/Entity Type

Health And Wellness

Colors

Requirements
Nice to have
• illustrations as per 2 sample images provided
• call to action if can fit

```html
<!DOCTYPE html>
<html lang="en">
<head>
<meta charset="utf-8">
<title>Holistic Health Coaching – I can help you</title>
<link rel="stylesheet" href="https://fonts.googleapis.com/css2?family=Kaushan+Script&display=swap">
<style>
  :root {
    --sky-glow: #f4fbff;
    --tree-dark: #2f4a2a;
    --tree-mid: #5b7a3c;
    --grass-light: #8fc160;
    --grass-deep: #4e8a2e;
    --portrait-top: #c69a7c;
    --portrait-mid: #ece7e2;
    --portrait-low: #1e2433;
    --cta-blue: #1f86c0;
    --cta-blue-light: #6fc0e6;
    --lifestyle-green: #4b7a2a;
    --health-brown: #6a3f22;
    --nutrition-navy: #0d1530;
    --ink-white: #ffffff;
    --sketch-tint: rgba(255,255,255,0.22);
  }
  * { margin: 0; padding: 0; box-sizing: border-box; }
  html, body { width: 1200px; height: 444px; overflow: hidden; background: #ffffff; }
  .banner {
    position: relative;
    width: 1200px;
    height: 444px;
    overflow: hidden;
    font-family: "Kaushan Script", cursive;
  }
  .park-scene {
    position: absolute; inset: 0;
    background:
      radial-gradient(ellipse 420px 170px at 640px 200px, var(--sky-glow) 0%, rgba(244,251,255,0.7) 40%, rgba(244,251,255,0) 100%),
      radial-gradient(circle 120px at 40px 20px, rgba(220,235,255,0.9), rgba(220,235,255,0) 100%),
      linear-gradient(180deg, var(--tree-dark) 0%, var(--tree-mid) 35%, var(--grass-light) 55%, var(--grass-deep) 100%);
  }
  .coach-portrait {
    position: absolute;
    left: 78px; top: 40px;
    width: 292px; height: 404px;
    border-radius: 140px 140px 0 0;
    background: linear-gradient(180deg, var(--portrait-top) 0%, var(--portrait-top) 30%, var(--portrait-mid) 42%, var(--portrait-mid) 72%, var(--portrait-low) 88%);
  }
  .sketch {
    position: absolute;
    border-radius: 50%;
    background: radial-gradient(closest-side, var(--sketch-tint) 0%, rgba(255,255,255,0.1) 60%, rgba(255,255,255,0) 100%);
  }
  .sketch--tea { left: 400px; top: 15px; width: 150px; height: 120px; }
  .sketch--dumbbell { left: 765px; top: 20px; width: 185px; height: 120px; }
  .sketch--heartbeat { left: 378px; top: 262px; width: 212px; height: 135px; }
  .sketch--carrot { left: 805px; top: 268px; width: 150px; height: 165px; }
  .sketch--basket { left: 978px; top: 140px; width: 200px; height: 160px; }
  .blobs { position: absolute; inset: 0; }
  .word { position: absolute; color: var(--ink-white); line-height: 1; white-space: nowrap; }
  .word--change {
    left: 8px; top: 352px;
    font-size: 104px;
    transform-origin: 0 0;
    transform: rotate(-90deg);
  }
  .word--holistic { left: 578px; top: 22px; font-size: 40px; text-align: center; line-height: 0.95; }
  .word--lifestyle { left: 998px; top: 50px; font-size: 46px; transform: rotate(-8deg); }
  .word--health { left: 634px; top: 368px; font-size: 36px; transform: rotate(-4deg); }
  .word--nutrition { left: 1010px; top: 355px; font-size: 42px; transform: rotate(6deg); }
  .call-to-action {
    position: absolute;
    left: 372px; top: 140px;
    font-size: 94px;
    font-weight: 400;
    line-height: 1.1;
    white-space: nowrap;
    background: linear-gradient(180deg, var(--cta-blue-light) 0%, var(--cta-blue) 70%);
    -webkit-background-clip: text;
    background-clip: text;
    color: transparent;
  }
</style>
</head>
<body>
<main class="banner">
  <div class="park-scene" role="img" aria-label="Sunlit park with trees and a green lawn"></div>
  <div class="coach-portrait" role="img" aria-label="Health coach sitting cross-legged on the grass"></div>

  <div class="sketch sketch--tea" role="img" aria-label="Line drawing of a coffee cup and teapot"></div>
  <div class="sketch sketch--dumbbell" role="img" aria-label="Line drawing of a dumbbell"></div>
  <div class="sketch sketch--heartbeat" role="img" aria-label="Line drawing of a heart with a heartbeat line"></div>
  <div class="sketch sketch--carrot" role="img" aria-label="Line drawing of a carrot"></div>
  <div class="sketch sketch--basket" role="img" aria-label="Line drawing of a basket of fruit and vegetables"></div>

  <svg class="blobs" width="1200" height="444" viewBox="0 0 1200 444" aria-hidden="true">
    <circle cx="1075" cy="72" r="112" fill="var(--lifestyle-green)"/>
    <circle cx="690" cy="384" r="66" fill="var(--health-brown)"/>
    <circle cx="1105" cy="378" r="112" fill="var(--nutrition-navy)"/>
  </svg>

  <span class="word word--change">Change</span>
  <span class="word word--holistic">holistic<br>health</span>
  <span class="word word--lifestyle">lifestyle</span>
  <span class="word word--health">health</span>
  <span class="word word--nutrition">nutrition</span>

  <h1 class="call-to-action">i can help you</h1>
</main>
</body>
</html>
```